Make a brochure for my cyber security company

I need a brochure (in english and french) for my cyber security company.

Company name: Brontavel Cyber
website: [login to view URL]
email: contact@[login to view URL]
Phone: xxxxxxxxxxx
Slogan: "Your Digital Shield" (english)
"Votre bouclier numerique" (french)
Attached is the logo

.......................Content (French Version)......................................
Qui nous sommes!

Brontavel Security est une équipe expérimentée et talentueuse d'expert en cybersécurité dont la mission principale est de fournir à nos clients les connaissances et l’expertise nécessaires pour défendre leurs entreprises contre les cyberattaques avancées. Nos capacités et méthodologies reposent sur plusieurs années consacrer a protéger des entreprises contre des attaques ciblées et menaces sophistiqués. Depuis plus de dix ans, notre équipe aide les clients à faire évoluer leurs capacités sur tout le spectre de personnes, de processus et de technologies, leur permettant ainsi de se défendre de manière proactive contre les cyberattaques avancées.

Nos services

Conseil stratégique
Services SOC
Gestion de la vulnérabilité et des risques
Audit et test de pénétration
Red team et Simulation d'adversaires avancée
Enquêtes judiciaires numériques
Services de témoins experts
Sécurité des systèmes de contrôle industriels (ICS/SCADA)
Réponse aux incidents et mesures correctives
Chasse à la menace (Threat Hunting)
Formation en cybersécurité

Industries que nous servons

Dans un monde interconnecté à l'échelle mondiale, de plus en plus de secteurs sont confrontés aux défis liés aux cyberattaques. Les entreprises sont confrontées a des risques qui permette a leurs adversaires voler leurs propriété intellectuelles, qui peuvent permettre au criminels de poursuivent des gains financiers a travers la fraude et le vol d’identité et perturber des opérations critiques. Chez "Brontavel Cyber", nos experts possèdent une expertise et une expérience approfondie du domaine pour aider nos clients à renforcer leurs capacités de cyber défenses pour se détecter et prévenir ces cyber-menaces sophistiquées. Notre équipe possède une profonde expérience dans les secteurs suivant:

Gouvernement et armée
Forces de l'ordre
justice
Technologie et communications
Banques et services financiers
Usine et fabrication
Transport
Santé
Petrole et Gas
Énergie et services publics

Content (English Version)

Who we are!

Brontavel Security is an experienced and talented team of cyber security professionals whose primary mission is to provide our clients with knowledge and expertise to defend their enterprises against advanced cyber attacks. Our capabilities and methodologies are based on over a decade of defending enterprises against targeted attacks and sophisticated threat actors. For over a decade, our team has helped clients evolve their capabilities across the full spectrum of people, process and technology enabling them to proactively defend against advanced cyber attacks.

Our Services

Strategic Consulting
SOC Services
Audit, Vulnerability & Risk Management
Penetration Testing, Red Team & Advanced Adversary Simulations
Digital Forensics Investigations
Expert Witness Services
Industrial Control Systems Security
Incident Response & Remediation
Cyber Security Training

Industries we serve

In a globally interconnected world, more and more industries are facing the challenges associated with cyber attacks. Companies face the risks of adversaries stealing intellectual property, criminals pursuing financial gain through fraud and identity theft, and attackers disrupting critical operations. At Brontavel Cyber, our experts have expertise and deep domain experience to help our clients evolve their cyber defenses to defend against these sophisticated cyber threats. Our team has deep experience in:

Government & Military
Law & Justice
Technology & Commutations
Financial Services
Manufacturing
Transportation
Health & Life sciences
Oil & Gas
Energy & Utilities

```html
<!DOCTYPE html>
<html lang="en">
<head>
<meta charset="utf-8">
<title>Brontavel Cyber — Brochure Outside</title>
<link rel="stylesheet" href="https://fonts.googleapis.com/css2?family=Source+Sans+3:wght@400;600;700&display=swap">
<style>
  :root {
    --navy: #1c2a5b;
    --navy-light: #2d4a86;
    --blue: #1a6db5;
    --blue-bright: #2a80c9;
    --line-soft: #dbe6f2;
    --white: #ffffff;
    --ink: #2a2a2a;
    --grey-soft: #e4e7ec;
  }
  html, body {
    margin: 0;
    padding: 0;
    overflow: hidden;
    background: var(--white);
  }
  .brochure {
    position: relative;
    width: 1200px;
    height: 849px;
    overflow: hidden;
    background: var(--white);
    font-family: "Source Sans 3", "Myriad Pro", sans-serif;
  }
  .art {
    position: absolute;
    inset: 0;
  }
  .decor {
    position: absolute;
  }
  .decor-tech-lines {
    left: 0;
    top: 102px;
    width: 400px;
    height: 80px;
    background: linear-gradient(90deg, var(--line-soft), rgba(219, 230, 242, 0.35));
  }
  .decor-cover-lines {
    left: 872px;
    top: 592px;
    width: 88px;
    height: 257px;
    background: linear-gradient(180deg, var(--navy), var(--navy-light));
  }
  .decor-flap-line {
    left: 1116px;
    top: 156px;
    width: 10px;
    height: 486px;
    background: linear-gradient(180deg, var(--grey-soft), rgba(228, 231, 236, 0.3));
  }
  .brand-text {
    font-weight: 600;
    fill: var(--navy);
    letter-spacing: 0.5px;
  }
  .experience-heading {
    font-weight: 700;
    font-size: 32px;
    fill: var(--blue);
  }
  .industry-label {
    font-size: 16.5px;
    fill: var(--white);
  }
  .hex-title {
    font-size: 50px;
    fill: var(--navy);
  }
  .slogan {
    font-size: 28px;
    font-weight: 700;
    fill: var(--blue);
  }
  .version {
    font-size: 21px;
    fill: var(--ink);
  }
  .contact-text {
    font-size: 17px;
    fill: var(--white);
  }
  .cover-slogan {
    font-size: 56px;
    fill: var(--white);
  }
  .cover-version {
    font-size: 23px;
    fill: var(--blue-bright);
  }
</style>
</head>
<body>
<div class="brochure">
  <svg class="art" width="1200" height="849" viewBox="0 0 1200 849" xmlns="http://www.w3.org/2000/svg">

    <!-- Inside flap: experience list -->
    <text class="experience-heading" x="29" y="336">Our team has deep</text>
    <text class="experience-heading" x="29" y="376">experience in:</text>

    <g class="industry-list">
      <g transform="translate(0,417)">
        <line x1="0" y1="0" x2="64" y2="0" stroke="var(--navy)" stroke-width="1.5"/>
        <rect x="57" y="-7" width="14" height="14" transform="rotate(45 64 0)" fill="var(--blue)" stroke="var(--navy)" stroke-width="1.5"/>
        <rect x="91" y="-12.5" width="309" height="25" fill="var(--navy)"/>
        <polygon points="91,-12.5 101,0 91,12.5" fill="var(--white)"/>
        <text class="industry-label" x="112" y="6">Government &amp; Military</text>
      </g>
      <g transform="translate(0,457)">
        <line x1="0" y1="0" x2="64" y2="0" stroke="var(--navy)" stroke-width="1.5"/>
        <rect x="57" y="-7" width="14" height="14" transform="rotate(45 64 0)" fill="var(--blue)" stroke="var(--navy)" stroke-width="1.5"/>
        <rect x="91" y="-12.5" width="309" height="25" fill="var(--navy)"/>
        <polygon points="91,-12.5 101,0 91,12.5" fill="var(--white)"/>
        <text class="industry-label" x="112" y="6">Law &amp; Justice</text>
      </g>
      <g transform="translate(0,496)">
        <line x1="0" y1="0" x2="64" y2="0" stroke="var(--navy)" stroke-width="1.5"/>
        <rect x="57" y="-7" width="14" height="14" transform="rotate(45 64 0)" fill="var(--blue)" stroke="var(--navy)" stroke-width="1.5"/>
        <rect x="91" y="-12.5" width="309" height="25" fill="var(--navy)"/>
        <polygon points="91,-12.5 101,0 91,12.5" fill="var(--white)"/>
        <text class="industry-label" x="112" y="6">Technology &amp; Commutations</text>
      </g>
      <g transform="translate(0,536)">
        <line x1="0" y1="0" x2="64" y2="0" stroke="var(--navy)" stroke-width="1.5"/>
        <rect x="57" y="-7" width="14" height="14" transform="rotate(45 64 0)" fill="var(--blue)" stroke="var(--navy)" stroke-width="1.5"/>
        <rect x="91" y="-12.5" width="309" height="25" fill="var(--navy)"/>
        <polygon points="91,-12.5 101,0 91,12.5" fill="var(--white)"/>
        <text class="industry-label" x="112" y="6">Financial Services</text>
      </g>
      <g transform="translate(0,575)">
        <line x1="0" y1="0" x2="64" y2="0" stroke="var(--navy)" stroke-width="1.5"/>
        <rect x="57" y="-7" width="14" height="14" transform="rotate(45 64 0)" fill="var(--blue)" stroke="var(--navy)" stroke-width="1.5"/>
        <rect x="91" y="-12.5" width="309" height="25" fill="var(--navy)"/>
        <polygon points="91,-12.5 101,0 91,12.5" fill="var(--white)"/>
        <text class="industry-label" x="112" y="6">Manufacturing</text>
      </g>
      <g transform="translate(0,614)">
        <line x1="0" y1="0" x2="64" y2="0" stroke="var(--navy)" stroke-width="1.5"/>
        <rect x="57" y="-7" width="14" height="14" transform="rotate(45 64 0)" fill="var(--blue)" stroke="var(--navy)" stroke-width="1.5"/>
        <rect x="91" y="-12.5" width="309" height="25" fill="var(--navy)"/>
        <polygon points="91,-12.5 101,0 91,12.5" fill="var(--white)"/>
        <text class="industry-label" x="112" y="6">Transportation</text>
      </g>
      <g transform="translate(0,655)">
        <line x1="0" y1="0" x2="64" y2="0" stroke="var(--navy)" stroke-width="1.5"/>
        <rect x="57" y="-7" width="14" height="14" transform="rotate(45 64 0)" fill="var(--blue)" stroke="var(--navy)" stroke-width="1.5"/>
        <rect x="91" y="-12.5" width="309" height="25" fill="var(--navy)"/>
        <polygon points="91,-12.5 101,0 91,12.5" fill="var(--white)"/>
        <text class="industry-label" x="112" y="6">Health &amp; Life</text>
      </g>
      <g transform="translate(0,694)">
        <line x1="0" y1="0" x2="64" y2="0" stroke="var(--navy)" stroke-width="1.5"/>
        <rect x="57" y="-7" width="14" height="14" transform="rotate(45 64 0)" fill="var(--blue)" stroke="var(--navy)" stroke-width="1.5"/>
        <rect x="91" y="-12.5" width="309" height="25" fill="var(--navy)"/>
        <polygon points="91,-12.5 101,0 91,12.5" fill="var(--white)"/>
        <text class="industry-label" x="112" y="6">Sciences</text>
      </g>
      <g transform="translate(0,733)">
        <line x1="0" y1="0" x2="64" y2="0" stroke="var(--navy)" stroke-width="1.5"/>
        <rect x="57" y="-7" width="14" height="14" transform="rotate(45 64 0)" fill="var(--blue)" stroke="var(--navy)" stroke-width="1.5"/>
        <rect x="91" y="-12.5" width="309" height="25" fill="var(--navy)"/>
        <polygon points="91,-12.5 101,0 91,12.5" fill="var(--white)"/>
        <text class="industry-label" x="112" y="6">Oil &amp; Gas</text>
      </g>
      <g transform="translate(0,772)">
        <line x1="0" y1="0" x2="64" y2="0" stroke="var(--navy)" stroke-width="1.5"/>
        <rect x="57" y="-7" width="14" height="14" transform="rotate(45 64 0)" fill="var(--blue)" stroke="var(--navy)" stroke-width="1.5"/>
        <rect x="91" y="-12.5" width="309" height="25" fill="var(--navy)"/>
        <polygon points="91,-12.5 101,0 91,12.5" fill="var(--white)"/>
        <text class="industry-label" x="112" y="6">Energy &amp; Utilities</text>
      </g>
    </g>

    <!-- Back panel: brand name -->
    <g class="brand-name">
      <circle cx="616" cy="130" r="22" fill="none" stroke="var(--navy)" stroke-width="2.5"/>
      <text class="brand-text" x="616" y="192" text-anchor="middle" font-size="16">BRONTAVEL CYBER</text>
    </g>

    <!-- Back panel: hexagon title -->
    <polygon points="436,366 478,296 722,296 764,366 722,437 478,437" fill="var(--white)" stroke="var(--navy)" stroke-width="2"/>
    <polygon points="442,366 481,301 719,301 758,366 719,432 481,432" fill="none" stroke="var(--blue)" stroke-width="4"/>
    <text class="hex-title" x="600" y="356" text-anchor="middle">Brontavel</text>
    <text class="hex-title" x="600" y="414" text-anchor="middle">Cyber</text>

    <text class="slogan" x="600" y="484" text-anchor="middle">Your Digital Shield</text>
    <text class="version" x="600" y="522" text-anchor="middle">English Version</text>

    <!-- Back panel: contact band -->
    <rect class="contact-band" x="400" y="684" width="400" height="100" fill="var(--navy)"/>
    <g class="contact-icons" fill="none" stroke="var(--white)" stroke-width="1.8">
      <path d="M486 696 l5 0 2 6 -3 3 q2 5 7 7 l3 -3 6 2 0 5 q-1 3 -4 3 q-16 -2 -18 -19 q0 -4 2 -4 z" fill="var(--white)" stroke="none"/>
      <circle cx="494" cy="734" r="9"/>
      <ellipse cx="494" cy="734" rx="4" ry="9"/>
      <line x1="485" y1="734" x2="503" y2="734"/>
      <rect x="484" y="757" width="20" height="14"/>
      <polyline points="484,757 494,765 504,757"/>
    </g>
    <text class="contact-text" x="531" y="709">+10 555 014 822</text>
    <text class="contact-text" x="531" y="739">www.brontavelcyber.com</text>
    <text class="contact-text" x="531" y="769">contact@brontavelcyber.com</text>

    <!-- Front cover: navy panel -->
    <rect class="cover-panel" x="800" y="0" width="233" height="849" fill="var(--navy)"/>
    <text class="cover-slogan" x="842" y="188">Your</text>
    <text class="cover-slogan" x="842" y="260">Digital</text>
    <text class="cover-slogan" x="842" y="332">Shield</text>
    <text class="cover-version" x="840" y="376">English Version</text>

    <!-- Front flap: brand name -->
    <g class="brand-name-small">
      <circle cx="1129" cy="62" r="18" fill="none" stroke="var(--navy)" stroke-width="2.2"/>
      <text class="brand-text" x="1129" y="110" text-anchor="middle" font-size="13">BRONTAVEL CYBER</text>
    </g>
  </svg>

  <div class="decor decor-tech-lines" role="img" aria-label="Decorative technology line motif in light blue"></div>
  <div class="decor decor-cover-lines" role="img" aria-label="Decorative technology line motif on the navy cover"></div>
  <div class="decor decor-flap-line" role="img" aria-label="Decorative vertical line motif in light grey"></div>
</div>
</body>
</html>
```